Web Design for photo printing service

Hi
I am looking for a new web design theme for our almost ready website http://fotoblik.zrmq.net, it will soon be launched under the name: www.zuna.is. (ZUNA means: You Only Live Once)

This is a website focused on printing photo products like: photo books, Greeting cards, posters, etc.

The whole theme should be playful, fun, creative. The marketing will be is that Life is fun, keep your memories. remember the good time etc.

So what I am looking for is a simple, yet colorful theme, easy to use.

We will be running max 4- 6 product groups, all extra info should be on the button,
expect shopping chart and sign in should be on top.

Extra feature:
Once a year during christmas, the web will turn on christmas outfit, it transforms
to Christmas looking Web. So a X-mas version would be fun to see !

Target Market(s)

Young people 20-35, young families.

Industry/Entity Type

Printing

Requirements
Must have
• Fun looking colorful design, simple to use.
Should not have
• Dark heavy look

```html
<!DOCTYPE html>
<html lang="en">
<head>
<meta charset="utf-8">
<title>ZUNA – Photo Printing</title>
<link rel="stylesheet" href="https://fonts.googleapis.com/css2?family=Fredoka:wght@400;500;600;700&family=Source+Sans+3:wght@400;600;700&display=swap">
<style>
:root{
  --sky-top:#bfe9f6;
  --sky-mid:#d6f0f8;
  --sky-low:#a9cdec;
  --teal:#0f9a78;
  --blue:#18a5cf;
  --aqua:#1aa6b0;
  --orange:#f7901e;
  --orange-dark:#e4700a;
  --grey:#666;
  --text:#555;
  --pink:#e31b54;
  --dark:#333031;
  --white:#fff;
  --magenta:#b0157f;
  --lime:#a6c91b;
  --placeholder:#e6ecf0;
}
*{margin:0;padding:0;box-sizing:border-box}
html,body{width:1200px;height:1050px;overflow:hidden;background:var(--white)}
body{position:relative;font-family:"Source Sans 3",sans-serif;color:var(--text)}
.abs{position:absolute}
.sky{left:0;top:0;width:1200px;height:438px;
  background:linear-gradient(180deg,var(--sky-top),var(--sky-mid) 45%,var(--sky-low))}
.social-top{left:202px;top:39px;display:flex;gap:4px}
.social-top span{width:24px;height:24px;border-radius:50%;background:var(--white);box-shadow:0 1px 2px rgba(0,0,0,.2)}
.social-top span:first-child{background:var(--teal)}
.pine{left:232px;top:76px;width:134px;height:44px;background:#7fb870;opacity:.55}
.brand{left:509px;top:28px;width:184px;text-align:center}
.brand-name{font-family:"Fredoka",sans-serif;font-weight:600;font-size:50px;line-height:58px;color:var(--aqua);display:inline-flex;align-items:center;gap:8px}
.brand-name i{width:14px;height:14px;border-radius:50%;background:var(--magenta)}
.brand-tag{font-size:8px;font-weight:700;color:#333;margin-top:-4px}
.account{left:869px;top:45px;display:flex;height:25px;font-size:11px}
.account .login{width:63px;background:linear-gradient(#fff,#e9e9e9);border:1px solid #ccc;color:#555;display:flex;align-items:center;justify-content:center}
.account .cart{width:69px;background:var(--teal);color:#fff;display:flex;align-items:center;justify-content:center;gap:4px}
.nav{left:218px;top:121px;width:749px;height:41px;background:var(--white);border-radius:20px;display:flex;box-shadow:0 6px 8px rgba(0,0,0,.12);font-family:"Fredoka",sans-serif;font-weight:500;font-size:14px;color:var(--teal)}
.nav a{display:flex;align-items:center;justify-content:center;border-right:1px solid #e2e2e2;color:inherit;text-decoration:none}
.nav .home{width:92px;background:var(--teal);color:#fff;font-weight:700;letter-spacing:1px;border-radius:20px 0 0 20px;border:none}
.hat{left:384px;top:212px;width:30px;height:50px;background:#d7262e;opacity:.85}
.headline{left:300px;top:212px;width:620px;text-align:center;font-family:"Fredoka",sans-serif;font-weight:700;color:var(--blue);letter-spacing:-1.5px}
.headline .l1,.headline .l2{font-size:43px;line-height:43px}
.headline .l3{font-size:34px;line-height:44px;color:var(--aqua);font-weight:600;letter-spacing:-1px}
.o1{color:var(--orange)}.o2{color:var(--magenta)}.o3{color:var(--lime)}
.products{left:196px;top:370px;width:820px;display:flex;justify-content:space-between}
.product{width:132px;text-align:center;position:relative}
.product .art{height:125px;margin:0 auto;width:120px;border-radius:8px;background:var(--placeholder)}
.product h3{font-family:"Fredoka",sans-serif;font-weight:700;font-size:17px;line-height:19px;color:var(--orange);margin-top:19px}
.product p{font-size:11px;line-height:13.5px;color:var(--grey);margin-top:4px}
.btn{position:absolute;left:11px;top:230px;width:92px;height:18px;border-radius:3px;background:linear-gradient(var(--orange),var(--orange-dark));color:#fff;font-size:8px;font-weight:700;display:flex;align-items:center;justify-content:center}
.divider{left:202px;top:649px;width:796px;height:1px;background:linear-gradient(90deg,transparent,#ddd 15%,#ddd 85%,transparent)}
.splash{left:200px;top:686px;width:96px;height:70px;background:#f3d3c0}
.welcome{left:302px;top:697px;display:flex;align-items:center;gap:14px;font-family:"Fredoka",sans-serif}
.welcome h2{font-weight:500;font-size:35px;color:var(--teal);letter-spacing:-1.5px}
.welcome .brand-name{font-size:32px;line-height:40px}
.welcome .brand-name i{width:10px;height:10px}
.intro{left:202px;top:758px;width:800px;font-size:14.2px;line-height:19.2px;color:var(--text)}
.more{left:202px;top:862px;font-weight:700;font-size:13.5px;color:#444}
.footer-dark{left:0;top:965px;width:1200px;height:85px;background:var(--dark)}
.footer-band{left:0;top:950px;width:1200px;height:20px;background:var(--pink);transform:skewY(-0.6deg)}
.footer-pink{left:217px;top:936px;width:766px;height:62px;background:var(--pink);border-radius:6px 6px 60% 60%/6px 6px 10px 10px;border-top:4px solid #dff3f6}
.footer-links{left:217px;top:959px;width:590px;text-align:right;color:#fff;font-size:17px}
.printer{left:847px;top:960px;display:flex;align-items:center;gap:6px;font-size:7px;color:#fff;line-height:8px}
.printer span{width:16px;height:16px;border-radius:50%;background:#fff}
.copy{left:202px;top:1016px;font-size:13px;color:#fff}
.social-foot{left:886px;top:1009px;display:flex;gap:8px}
.social-foot span{width:22px;height:22px;border-radius:50%;background:#eee}
</style>
</head>
<body>
<div class="sky abs"></div>

<div class="social-top abs"><span></span><span></span><span></span></div>
<div class="pine abs" role="img" aria-label="Pine branch with red baubles"></div>

<div class="brand abs">
  <div class="brand-name">ZUNA<i></i></div>
  <div class="brand-tag">you only live once</div>
</div>

<div class="account abs">
  <div class="login">LOGIN</div>
  <div class="cart">
    <svg width="14" height="11" viewBox="0 0 14 11"><path d="M0 1h3l2 6h7l1-4H4" fill="none" stroke="#fff" stroke-width="1.3"/><circle cx="6" cy="9.5" r="1" fill="#fff"/><circle cx="11" cy="9.5" r="1" fill="#fff"/></svg>
    MY CART
  </div>
</div>

<nav class="nav abs">
  <a class="home" href="#">HOME</a>
  <a href="#" style="width:102px">Photo Books</a>
  <a href="#" style="width:92px">Calendars</a>
  <a href="#" style="width:73px">Posters</a>
  <a href="#" style="width:137px">Opportunities Map</a>
  <a href="#" style="width:151px">Printed Photographs</a>
  <a href="#" style="width:102px;border:none">Our Price</a>
</nav>

<div class="hat abs" role="img" aria-label="Santa hat on the headline"></div>
<div class="headline abs">
  <div class="l1">Life Is Fun, Keep Your</div>
  <div class="l2">Memories &amp;</div>
  <div class="l3">Remember The G<span class="o1">o</span><span class="o2">o</span><span class="o3">d</span> Time</div>
</div>

<section class="products abs">
  <div class="product">
    <div class="art" role="img" aria-label="Notebook and pen illustration"></div>
    <h3>PHOTO BOOKS</h3>
    <p>Your Own Photographs? Why? We Know That Your Images Deserve To Be Preserved.</p>
    <div class="btn">VIEW DETAILS »</div>
  </div>
  <div class="product">
    <div class="art" role="img" aria-label="Print report sheets illustration"></div>
    <h3>CALENDARS</h3>
    <p>Your Own Photographs? Why? We Know That Your Images Deserve To Be Preserved.</p>
    <div class="btn">VIEW DETAILS »</div>
  </div>
  <div class="product">
    <div class="art" role="img" aria-label="Sunflower with arrow illustration" style="background:#eef0d8"></div>
    <h3>POSTERS</h3>
    <p>Your Own Photographs? Why? We Know That Your Images Deserve To Be Preserved.</p>
    <div class="btn">VIEW DETAILS »</div>
  </div>
  <div class="product">
    <div class="art" role="img" aria-label="Pen drawing a curve illustration"></div>
    <h3>OPPORTUNITIES MAP</h3>
    <p>Your Own Photographs? Why? We Know That Your Images Deserve.</p>
    <div class="btn">VIEW DETAILS »</div>
  </div>
  <div class="product">
    <div class="art" role="img" aria-label="Large format printer illustration"></div>
    <h3>PRINTED PHOTOGRAPHS</h3>
    <p>Your Own Photographs? Why? We Know That Your Images Deserve.</p>
    <div class="btn">VIEW DETAILS »</div>
  </div>
</section>

<div class="divider abs"></div>

<div class="splash abs" role="img" aria-label="Colourful paint splash decoration"></div>
<div class="welcome abs">
  <h2>WELCOME TO</h2>
  <div class="brand-name">ZUNA<i></i></div>
</div>

<p class="intro abs">Lorem Ipsum Dolor Sit Amet, Consectetuer Adipiscing Elit, Sed Diam Nonummy Nibh Euismod Tincidunt Ut Laoreet Dolore Magna Aliquam Erat Volutpat. Ut Wisi Enim Ad Minim Veniam, Quis Nostrud Exerci Tation Ullamcorper Suscipit Lobortis Nisl Ut Aliquip Ex Ea Commodo Consequat. Duis Autem Vel Eum Iriure Dolor In Hendrerit In Vulputate Velit Esse Molestie Consequat, Vel Illum Dolore Eu Feugiat Nulla Facilisis At Vero Eros Et Accumsan Et Iusto Odio Dignissim Qui Blandit Praesent Luptatum Zzril Delenit Augue Duis Dolore Te Feugait Nulla Facilisi.</p>
<div class="more abs">READ MORE</div>

<footer>
  <div class="footer-dark abs"></div>
  <div class="footer-band abs"></div>
  <div class="footer-pink abs"></div>
  <div class="footer-links abs">Heim | Smáa letrið | Hvað viltu vita | Verð | Um okkur | Samband</div>
  <div class="printer abs"><div>Prentað<br>hjá</div><span></span></div>
  <div class="copy abs">Copyright © 2013 Fotoblik All Rights Reserved.</div>
  <div class="social-foot abs"><span></span><span></span><span></span><span></span></div>
</footer>
</body>
</html>
```